Business Card Design Project

Use newly designed logo and tie into newly designed website
I need a new logo and website layout designed for my partner's business. This is a birthday present. His business is interior painting, wallpapering and design. He also has access to a wide variety of products including carpet, fabrics, furniture, wallpaper, tile, countertops, etc. I have attached some screen shots of his website for reference. He is a one man shop and has a stellar reputation with his customers. He is on-time, very tidy, excellent with animals, and always finishes on time and on budget. There are no restrictions on colors or fonts. The logo needs to work well with the website, business cards and printed materials. The website needs to flow content for device size so it looks just as good on a cell phone or tablet as it does on a desktop computer. Whatever the heck that's called!Thanks. I am looking forward to seeing everyone's ideas.
Updates
Hi Designers,
We've reopened this project as our logo design project has just completed.
Please refer to the uploaded files and make use of either Horizontal or Vertical versions of the logo depending on what you think is suitable for your design proposals.
We look forward to your creative submissions!
Target Market(s)
Consumers looking to improve the interior environment of their homes by updating wall paint or paper, flooring (either carpet, tile, or hardwoods), counter tops, window treatments, etc. Clients tend to be more upper middle class and have certain taste levels and expectations. New logo, website and business card should align to meet those levels.
Industry/Entity Type
Cell Phone
Look and feel
Each slider illustrates characteristics of the customer's brand and the style your logo design should communicate.

```html
<!DOCTYPE html>
<html lang="en">
<head>
<meta charset="utf-8">
<title>Marvella Interior Designs – Business Card</title>
<link rel="stylesheet" href="https://fonts.googleapis.com/css2?family=Cormorant+Garamond:wght@600&family=Crimson+Text&family=Open+Sans:wght@400&display=swap">
<style>
  :root {
    --backdrop: #e9e7e4;
    --card: #ffffff;
    --panel-grey: #cfcfcf;
    --brand-red: #8c1c1f;
    --brand-red-dark: #6a1214;
    --ink: #2b2b2b;
  }
  html, body {
    margin: 0;
    width: 1200px;
    height: 889px;
    overflow: hidden;
    background: var(--backdrop);
  }
  .business-card {
    position: absolute;
    left: 150px;
    top: 187px;
    width: 900px;
    height: 514px;
    background: var(--card);
    box-shadow: 0 10px 30px rgba(0,0,0,0.15);
    overflow: hidden;
  }
  .card-art {
    position: absolute;
    inset: 0;
    width: 100%;
    height: 100%;
  }
  .brand-name {
    position: absolute;
    left: 56px;
    top: 92px;
    margin: 0;
    font-family: "Cormorant Garamond", serif;
    font-weight: 600;
    font-size: 46px;
    color: var(--brand-red);
    letter-spacing: 0.5px;
  }
  .tagline {
    position: absolute;
    left: 60px;
    top: 160px;
    margin: 0;
    font-family: "Crimson Text", serif;
    font-size: 36px;
    color: var(--brand-red);
  }
  .contact-list {
    position: absolute;
    left: 50px;
    top: 352px;
    margin: 0;
    padding: 0;
    list-style: none;
    font-family: "Open Sans", sans-serif;
    font-size: 17px;
    color: var(--ink);
  }
  .contact-item {
    display: flex;
    align-items: center;
    gap: 14px;
    height: 40px;
  }
  .contact-icon {
    width: 28px;
    height: 28px;
    flex: none;
  }
</style>
</head>
<body>
  <main class="business-card">
    <svg class="card-art" viewBox="0 0 900 514" aria-hidden="true">
      <defs>
        <clipPath id="left-of-cross-ribbon">
          <path d="M600,514 C650,360 700,262 790,212 S880,182 910,180 L910,-10 L-10,-10 L-10,514 Z"/>
        </clipPath>
      </defs>
      <path class="grey-panel"
            d="M-10,300 C320,300 600,272 720,222 C800,188 860,112 910,60 L910,514 L-10,514 Z"
            fill="var(--panel-grey)" clip-path="url(#left-of-cross-ribbon)"/>
      <g fill="none" stroke="var(--brand-red)" stroke-width="7" stroke-linecap="round">
        <path class="ribbon-main" d="M-10,300 C320,300 600,272 720,222 C800,188 860,112 910,60"/>
        <path class="ribbon-cross" d="M600,520 C650,360 700,262 790,212 S880,182 910,180"/>
      </g>
      <g fill="none" stroke="var(--brand-red-dark)" stroke-width="1.5" opacity="0.6">
        <path d="M-10,305 C320,305 602,277 722,227 C802,193 862,117 910,66"/>
        <path d="M606,520 C655,363 705,267 793,218 S882,188 910,186"/>
      </g>
    </svg>

    <h1 class="brand-name">Marvella Interior Designs</h1>
    <p class="tagline">. . . beautiful happens.</p>

    <ul class="contact-list">
      <li class="contact-item">
        <svg class="contact-icon" viewBox="0 0 28 28" aria-hidden="true">
          <circle cx="14" cy="14" r="14" fill="var(--brand-red)"/>
          <path d="M9 8 h3 l1 4 -2 1.5 q1.5 3 4 4.5 l1.5-2 4 1 v3 q-1 1.5 -3 1.5 q-9-2 -10-11 q0-2 1.5-2.5z" fill="#fff"/>
        </svg>
        <span>000-000-0000</span>
      </li>
      <li class="contact-item">
        <svg class="contact-icon" viewBox="0 0 28 28" aria-hidden="true">
          <circle cx="14" cy="14" r="14" fill="var(--brand-red)"/>
          <rect x="7" y="9" width="14" height="10" fill="#fff"/>
          <path d="M7 9 L14 15 L21 9" fill="none" stroke="var(--brand-red)" stroke-width="1.4"/>
        </svg>
        <span>Youremail@</span>
      </li>
      <li class="contact-item">
        <svg class="contact-icon" viewBox="0 0 28 28" aria-hidden="true">
          <circle cx="14" cy="14" r="14" fill="var(--brand-red)"/>
          <g fill="none" stroke="#fff" stroke-width="1.4">
            <circle cx="14" cy="14" r="7"/>
            <ellipse cx="14" cy="14" rx="3" ry="7"/>
            <path d="M7 14 H21 M8.5 10.5 H19.5 M8.5 17.5 H19.5"/>
          </g>
        </svg>
        <span>Youtwebsite</span>
      </li>
    </ul>
  </main>
</body>
</html>
```